Blue Ladle Handcrafted Tomato Ketchup packaging design modern

From the best ingredients there is the best ketchup Blue Handcrafted ketchup are specially formulated for fine dining and drinks, bringing out all the flavors. As the Blue Ladle handcrafted ketchup is otherwise fabulous: Made with wholesome, fully ripe fruits Nothing with half things! All Blue Ladle handcrafted ketchups are pure nature, without any artificial diluents or concentrates. Where tomato is on it, that's all there is to it - guaranteed! the design should be professional and noble despite being trendy. A watcher wants to sell the ketchup as merchandising from our restaurant. but as a single brand positioning. The ketchup is vegan. Dimensions: 6.8 cm Height: 7.8 cm Circumference: 21.6 cm The text down (Text 1-4). The lid of the text the glass packaging is black! Thanks for your efforts. I look forward to your designs.

Target Market(s)

foodies

Font styles to use
Serif
Sans Serif

Colors

Designer to choose colors to be used in the design.

Requirements
Must have
• Title: (Handcrafted Tomato Ketchup) Text One: (Store chilled after opening and consume quickly, pasteurized.) Text Two: (Handcrafted in Switzerland by Brennwald Kulinarik GmbH, Chur www.blueladle-sample.ch) Text Tree: (Tomatoes, White Wine Vinegar, Aceto Balsamico, Brown Cane Sugar, Corn Starch, Spices, Salt) Text For: (200 grams) or (200g) The Logo of Blue Ladle with the Pasta and Wine have to because of the gesety.
Nice to have
• small vegan icon (maybe)
Should not have
• text of the logo (pasta & wine)

```html
<!DOCTYPE html>
<html lang="en">
<head>
<meta charset="UTF-8">
<title>Blue Ladle – Handcrafted Tomato Ketchup Label</title>
<link rel="stylesheet" href="https://fonts.googleapis.com/css2?family=Josefin+Sans:wght@300;400&family=Yanone+Kaffeesatz:wght@700&display=swap">
<style>
  :root {
    --page-bg: #eef0f3;
    --label-cream: #d9c39a;
    --label-teal: #3f8584;
    --label-teal-light: #4f9897;
    --ink: #1d2a2c;
    --ribbon-orange: #e69a43;
    --ribbon-shadow: #b9742c;
    --ribbon-ink: #3a2412;
  }
  html, body {
    margin: 0;
    padding: 0;
    width: 1200px;
    height: 1200px;
    overflow: hidden;
    background: var(--page-bg);
  }
  .canvas {
    position: relative;
    width: 1200px;
    height: 1200px;
  }
  .label {
    position: absolute;
    left: 210px;
    top: 140px;
    width: 780px;
    height: 920px;
    background: var(--label-cream);
    box-sizing: border-box;
    padding: 22px 0;
  }
  .label-panel {
    position: relative;
    width: 100%;
    height: 100%;
    background: linear-gradient(100deg, var(--label-teal-light) 0%, var(--label-teal) 45%, var(--label-teal) 70%, var(--label-teal-light) 100%);
    color: var(--ink);
    font-family: "Josefin Sans", sans-serif;
    text-align: center;
  }
  .brand-name {
    position: absolute;
    top: 160px;
    left: 0;
    right: 0;
    margin: 0;
    font-weight: 400;
    font-size: 88px;
    letter-spacing: 0.18em;
    line-height: 1;
    padding-left: 0.18em;
  }
  .title-ribbon {
    position: absolute;
    top: 268px;
    left: 140px;
    width: 500px;
    height: 76px;
  }
  .title-ribbon svg {
    position: absolute;
    inset: 0;
  }
  .product-title {
    position: relative;
    margin: 0;
    line-height: 70px;
    font-family: "Yanone Kaffeesatz", sans-serif;
    font-weight: 700;
    font-size: 40px;
    color: var(--ribbon-ink);
    letter-spacing: 0.01em;
  }
  .storage-note {
    position: absolute;
    top: 430px;
    left: 0;
    right: 0;
    margin: 0;
    font-size: 25px;
    font-weight: 300;
    line-height: 36px;
  }
  .maker-info,
  .ingredients,
  .net-weight {
    position: absolute;
    left: 0;
    right: 0;
    margin: 0;
    font-size: 18px;
    font-weight: 300;
    line-height: 25px;
  }
  .maker-info { top: 585px; }
  .ingredients { top: 690px; }
  .net-weight { top: 782px; }
</style>
</head>
<body>
<main class="canvas">
  <section class="label">
    <div class="label-panel">
      <h1 class="brand-name">BLUE LADLE</h1>

      <div class="title-ribbon">
        <svg viewBox="0 0 500 76" width="500" height="76" aria-hidden="true">
          <polygon points="0,22 48,22 48,72 0,72 18,47" fill="var(--ribbon-shadow)"/>
          <polygon points="500,22 452,22 452,72 500,72 482,47" fill="var(--ribbon-shadow)"/>
          <rect x="30" y="6" width="440" height="58" fill="var(--ribbon-orange)"/>
        </svg>
        <h2 class="product-title">HANDCRAFTED TOMATO KETCHUP</h2>
      </div>

      <p class="storage-note">Store chilled<br>after opening and consume quickly, pasteurized.</p>

      <p class="maker-info">Handcrafted in Switzerland<br>by Brennwald Kulinarik GmbH, Chur<br>www.blueladle-sample.ch</p>

      <p class="ingredients">Tomatoes, White Wine Vinegar, Aceto Balsamico,<br>Brown Cane Sugar, Corn Starch, Spices, Salt</p>

      <p class="net-weight">200 grams</p>
    </div>
  </section>
</main>
</body>
</html>
```